Emergency Medical Training and Events Company Business Needs Business Card Design

We are in need of a business card for our dynamic company expanding its customer base and need to be easily contacted and identified for when we visit with government officials, potential EMS / Fire agencies and county coordinators to arrange for training programs for first responders to better prepare them for critical thinking at critical incidents.

Target Market(s)

EMS/Fire and Event Promoters

Industry/Entity Type

Medical

Contact Information for Business Card

Two cards, comparable designs:

Martin K. Halvey, Principal, m.halvey@rvqtlo.com
Owen Tash, Event and Training Specialist, o.tash@rvqtlo.com

Font styles to use
Other font styles liked:
• Cambria

Colors

Designer to choose colors to be used in the design.

Requirements
Must have
• Company Logo, Spots for Name, Title, Phone Number, Email, Website
• A bullet list stating that we offer, QRB CPR and First Aid Instructors, Hold the Line Instructors, Event EMS, CME's, MCI Training and Planning. We prefer to have a black background for the card but if you can make a blue or white card stand out we would review that as well.
Should not have
• Tacky logos or special sayings ... simple, elegant, professional is the look we seek

```html
<!DOCTYPE html>
<html lang="en">
<head>
<meta charset="utf-8">
<title>RVQ Solutions – Business Card</title>
<link rel="stylesheet" href="https://fonts.googleapis.com/css2?family=Caladea:ital,wght@0,400;0,700;1,700&family=Poppins:wght@600&display=swap">
<style>
  :root{
    --navy:#1c1d4d;
    --red:#c42128;
    --paper:#f1f1f2;
    --white:#ffffff;
    --backdrop:#e8e8e7;
  }
  *{margin:0;padding:0;box-sizing:border-box}
  html,body{width:1200px;height:980px;overflow:hidden;background:var(--backdrop)}
  .canvas{position:relative;width:1200px;height:980px}
  .card{
    position:absolute;top:221px;width:335px;height:587px;
    border-radius:16px;overflow:hidden;
  }
  .card--front{left:243px}
  .card--back{left:634px}
  .card-bg{position:absolute;inset:0;width:100%;height:100%;display:block}
  .brand{
    position:absolute;left:0;right:0;top:74px;
    display:flex;align-items:center;justify-content:center;gap:12px;
  }
  .brand-dot{width:58px;height:58px;border-radius:50%;background:var(--white);flex:none}
  .brand-name{
    font-family:"Caladea",Cambria,serif;font-weight:700;color:var(--white);
    font-size:22px;line-height:1.05;
  }
  .person{position:absolute;left:0;right:0;top:268px;text-align:center}
  .person-name{
    font-family:"Poppins",sans-serif;font-weight:600;color:var(--red);
    font-size:27px;line-height:1.15;
  }
  .person-title{
    font-family:"Caladea",Cambria,serif;font-weight:700;color:var(--navy);
    font-size:20px;line-height:1.1;
  }
  .contact{
    position:absolute;left:0;right:0;top:434px;text-align:center;
    font-family:"Caladea",Cambria,serif;color:var(--white);font-size:19px;line-height:27px;
  }
  .contact p+p.gap{margin-top:16px}
  .back-brand{
    position:absolute;left:0;right:0;top:70px;text-align:center;
  }
  .back-brand .brand-dot{width:130px;height:130px;margin:0 auto 20px}
  .back-brand .brand-name{font-size:26px}
  .services{
    position:absolute;left:34px;top:446px;list-style:none;
    font-family:"Caladea",Cambria,serif;font-style:italic;font-weight:700;
    color:var(--white);font-size:16.5px;line-height:31px;
  }
  .services li{position:relative;padding-left:24px}
  .services li::before{
    content:"";position:absolute;left:0;top:12px;width:9px;height:9px;border-radius:50%;background:var(--white);
  }
</style>
</head>
<body>
<main class="canvas">

  <section class="card card--front">
    <svg class="card-bg" viewBox="0 0 335 587" preserveAspectRatio="none" aria-hidden="true">
      <rect width="335" height="587" fill="var(--paper)"/>
      <path d="M0 0H335V160C270 180 230 225 168 226C105 226 65 180 0 160Z" fill="var(--navy)"/>
      <path d="M0 160C65 180 105 226 168 226C230 225 270 180 335 160" fill="none" stroke="var(--red)" stroke-width="7"/>
      <path d="M0 430C65 405 105 360 168 360C230 360 270 405 335 430V587H0Z" fill="var(--red)"/>
      <path d="M0 430C65 405 105 360 168 360C230 360 270 405 335 430" fill="none" stroke="var(--navy)" stroke-width="7"/>
    </svg>
    <div class="brand">
      <span class="brand-dot"></span>
      <span class="brand-name">RVQ Solutions<br>of TLO</span>
    </div>
    <div class="person">
      <h1 class="person-name">Martin K. Halvey</h1>
      <p class="person-title">Principal</p>
    </div>
    <div class="contact">
      <p>M: 123 456 7890<br>Ph: 321 654 9870</p>
      <p class="gap">m.halvey@rvqtlo.com<br>www.rvqtlo.com</p>
    </div>
  </section>

  <section class="card card--back">
    <svg class="card-bg" viewBox="0 0 335 587" preserveAspectRatio="none" aria-hidden="true">
      <rect width="335" height="587" fill="var(--navy)"/>
      <path d="M0 427C60 400 110 360 165 358C225 358 275 400 335 427V587H0Z" fill="var(--red)"/>
      <path d="M0 427C60 400 110 360 165 358C225 358 275 400 335 427" fill="none" stroke="var(--white)" stroke-width="2.5"/>
    </svg>
    <div class="back-brand">
      <div class="brand-dot"></div>
      <p class="brand-name">RVQ Solutions of TLO</p>
    </div>
    <ul class="services">
      <li>QRB CPR &amp; First Aid Instructors</li>
      <li>Event EMS, CME's</li>
      <li>Hold the Line Instructors</li>
      <li>MCI Training &amp; Planning</li>
    </ul>
  </section>

</main>
</body>
</html>
```